Brightway Carpet and Tile cleaning Business card Design

I need a design that has the same feel as my van.
i would also like a prominent "Review us on facebook" somewhere, but not that it makes it look silly.
I would like the card to have a little bit of grey or black in the design as well.

It will need contact details
phone: 0498 716254
email: rkbrightwayclean@mailvista.com
website: www.brightwaycarpetandtilecleaning.com.au
facebook: /brightwaycarpetandtilecleaning

Industry/Entity Type

Business

Contact Information for Business Card

Phone number 0498716254
Email rkbrightwayclean@mailvista.com
Website www.brightwaycarpetandtilecleaning.com.au
Facebook/brightwaycarpetandtilecleaning

Colors
000000

Requirements
Must have
• Same feel as my van
• I want the card to stand out from the crowd
Nice to have
• Maybe include a tiny bit of a third colour? Grey's,blacks, orange?

```html
<!DOCTYPE html>
<html lang="en">
<head>
<meta charset="utf-8">
<title>Brightway Carpet and Tile cleaning — Business Card</title>
<link rel="stylesheet" href="https://fonts.googleapis.com/css2?family=Montserrat:wght@700&family=Questrial&display=swap">
<style>
  :root {
    --page: #e9e6e1;
    --card: #0b0c0d;
    --bubble-dark: #1b1d1f;
    --bubble-mid: #24272a;
    --cyan: #22b8d8;
    --green: #a9cf4a;
    --grey: #9aa0a4;
  }
  * { margin: 0; padding: 0; box-sizing: border-box; }
  html, body {
    width: 1200px; height: 780px; overflow: hidden;
    background: var(--page);
  }
  .canvas {
    width: 1200px; height: 780px;
    display: flex; align-items: center; justify-content: center; gap: 48px;
  }
  .card {
    position: relative;
    width: 540px; height: 330px;
    border-radius: 18px;
    background: var(--card);
    overflow: hidden;
    box-shadow: 0 10px 28px rgba(0,0,0,.28);
  }
  .card__pattern {
    position: absolute; inset: 0;
    background:
      radial-gradient(circle at 22% 30%, var(--bubble-mid) 0, transparent 38%),
      radial-gradient(circle at 78% 70%, var(--bubble-dark) 0, transparent 45%),
      radial-gradient(circle at 60% 15%, var(--bubble-dark) 0, transparent 30%),
      var(--card);
  }
  .brand {
    position: absolute;
    display: flex; align-items: center; gap: 12px;
    white-space: nowrap;
  }
  .brand__dot {
    width: 24px; height: 24px; border-radius: 50%;
    background: var(--cyan);
  }
  .brand__name {
    font-family: "Montserrat", sans-serif; font-weight: 700;
    color: var(--cyan); letter-spacing: -1px; line-height: 1;
  }
  .brand__tagline {
    position: absolute;
    font-family: "Questrial", sans-serif; color: var(--grey);
    font-size: 13px; letter-spacing: 2.5px; text-transform: uppercase;
    white-space: nowrap;
  }
  /* front */
  .front .brand { left: 36px; top: 74px; }
  .front .brand__name { font-size: 44px; }
  .front .brand__tagline { left: 72px; top: 128px; }
  .owner { position: absolute; right: 34px; top: 28px; text-align: right; white-space: nowrap; }
  .owner__name {
    font-family: "Montserrat", sans-serif; font-weight: 700;
    color: var(--cyan); font-size: 18px;
  }
  .owner__role {
    font-family: "Questrial", sans-serif; color: var(--green);
    font-size: 13px; margin-top: 2px;
  }
  .divider {
    position: absolute; left: 36px; right: 34px; top: 166px;
    height: 1px; background: var(--green); opacity: .8;
  }
  .contacts {
    position: absolute; left: 36px; top: 182px;
    list-style: none;
    font-family: "Questrial", sans-serif; color: var(--cyan);
    font-size: 15px;
  }
  .contacts li { display: flex; align-items: center; gap: 10px; height: 30px; white-space: nowrap; }
  .contact__icon {
    width: 20px; height: 20px; border-radius: 4px;
    background: var(--green);
    display: flex; align-items: center; justify-content: center;
    flex: none;
  }
  .contact__icon svg { width: 14px; height: 14px; }
  /* back */
  .back .brand { left: 50%; top: 100px; transform: translateX(-50%); }
  .back .brand__name { font-size: 50px; }
  .back .brand__tagline { left: 0; right: 0; top: 162px; text-align: center; }
  .review {
    position: absolute; left: 0; right: 0; top: 226px; text-align: center;
    font-family: "Questrial", sans-serif; color: var(--green); font-size: 19px;
  }
</style>
</head>
<body>
<main class="canvas">
  <section class="card front">
    <div class="card__pattern" role="img" aria-label="Dark background with soft grey bubble pattern"></div>
    <div class="owner">
      <div class="owner__name">Marco Delvecchio</div>
      <div class="owner__role">Owner/operator</div>
    </div>
    <div class="brand">
      <span class="brand__dot"></span>
      <span class="brand__name">Brightway</span>
    </div>
    <div class="brand__tagline">Carpet &amp; Tile Cleaning</div>
    <div class="divider"></div>
    <ul class="contacts">
      <li>
        <span class="contact__icon"><svg viewBox="0 0 24 24"><path d="M6.6 10.8a15.1 15.1 0 0 0 6.6 6.6l2.2-2.2a1 1 0 0 1 1-.25 11.4 11.4 0 0 0 3.6.57 1 1 0 0 1 1 1V20a1 1 0 0 1-1 1A17 17 0 0 1 3 4a1 1 0 0 1 1-1h3.5a1 1 0 0 1 1 1c0 1.25.2 2.45.57 3.57a1 1 0 0 1-.25 1z" fill="#0b0c0d"/></svg></span>
        0498 716254
      </li>
      <li>
        <span class="contact__icon"><svg viewBox="0 0 24 24"><rect x="3" y="6" width="18" height="12" rx="1.5" fill="none" stroke="#0b0c0d" stroke-width="2"/><path d="M3.5 7l8.5 6 8.5-6" fill="none" stroke="#0b0c0d" stroke-width="2"/></svg></span>
        rkbrightwayclean@mailvista.com
      </li>
      <li>
        <span class="contact__icon"><svg viewBox="0 0 24 24"><circle cx="12" cy="12" r="8.5" fill="none" stroke="#0b0c0d" stroke-width="2"/><path d="M3.5 12h17M12 3.5c-3 3-3 14 0 17M12 3.5c3 3 3 14 0 17" fill="none" stroke="#0b0c0d" stroke-width="1.6"/></svg></span>
        www.brightwaycarpetandtilecleaning.com.au
      </li>
      <li>
        <span class="contact__icon"></span>
        /brightwaycarpetandtilecleaning
      </li>
    </ul>
  </section>

  <section class="card back">
    <div class="card__pattern" role="img" aria-label="Dark background with soft grey bubble pattern"></div>
    <div class="brand">
      <span class="brand__dot"></span>
      <span class="brand__name">Brightway</span>
    </div>
    <div class="brand__tagline">Carpet &amp; Tile Cleaning</div>
    <div class="review">review us on Friendloop</div>
  </section>
</main>
</body>
</html>
```